PowerPoint Template for Consultancy Company.

We need a Power Point template for a Consultancy company based in Copenhagen, Denmark. We focus on supporting people and small companies in starting up next generation technology companies. Company name is "Vorstrup-Kjær Consulting". The template shall demonstrate growth, agility, next generation technology and following your dreams. Please include the uploaded logo.
Updates
Hi guys,
thanks for helping me on this project.
I like the font "Good Times" that is being used in my logo. I will like this to be used as minimum in the headlines in my power point template. I am not sure if it will work on standard text - but will relay on your judgement.
Kind regards
Torlak
Colors
Designer to choose colors to be used in the design.
Look and feel
Each slider illustrates characteristics of the customer's brand and the style your logo design should communicate.

```html
<!DOCTYPE html>
<html lang="en">
<head>
<meta charset="utf-8">
<title>Vorstrup-Kjær Consulting – Presentation Template Overview</title>
<link rel="stylesheet" href="https://fonts.googleapis.com/css2?family=Oswald:wght@500&family=Open+Sans:wght@400&display=swap">
<style>
  :root {
    --tan: #d49e6a;
    --paper: #ffffff;
    --ink: #111111;
    --muted: #444444;
    --navy: #232a6b;
    --divider: #e9c9a6;
    --blue-dark: #3a5da0;
    --blue-mid: #4f7fc2;
    --blue-light: #a9badb;
    --grid: #d9d9d9;
  }
  * { box-sizing: border-box; margin: 0; padding: 0; }
  html, body { width: 1200px; height: 1200px; overflow: hidden; background: var(--tan); }
  .board { position: absolute; left: 24px; top: 61px; width: 1153px; height: 1080px; background: var(--paper); }
  .slide { position: absolute; width: 384px; height: 216px; overflow: hidden; background: var(--paper);
           border-right: 1px solid var(--divider); border-bottom: 1px solid var(--divider); }
  .c1 { left: 0; } .c2 { left: 384px; } .c3 { left: 768px; width: 385px; border-right: none; }
  .r1 { top: 0; } .r2 { top: 216px; } .r3 { top: 432px; } .r4 { top: 648px; } .r5 { top: 864px; border-bottom: none; }
  .abs { position: absolute; }
  .title { position: absolute; font-family: "Oswald", "Arial Narrow", sans-serif; font-weight: 500;
           color: var(--ink); font-size: 25px; line-height: 1; white-space: nowrap; letter-spacing: -0.2px; }
  .body { position: absolute; font-family: "Open Sans", Arial, sans-serif; font-size: 4.6px; line-height: 8.6px; color: var(--muted); }
  .tag { position: absolute; font-family: "Oswald", "Arial Narrow", sans-serif; font-size: 3.6px; letter-spacing: 0.3px;
         color: #777; text-transform: uppercase; white-space: nowrap; }
  .tag.vertical { writing-mode: vertical-rl; }
  .photo { position: absolute; }
  .brand { position: absolute; display: flex; align-items: center; gap: 9px; }
  .brand-mark { width: 38px; height: 38px; background: var(--navy); }
  .brand-name { font-family: "Oswald", "Arial Narrow", sans-serif; font-weight: 500; color: var(--navy);
                font-size: 17px; line-height: 1.15; letter-spacing: 1.6px; text-transform: uppercase; }
  .chart { position: absolute; left: 0; top: 0; }
  .chart text { font-family: "Open Sans", Arial, sans-serif; font-size: 8.5px; fill: #222; }
</style>
</head>
<body>
<div class="board">

  <!-- Row 1 -->
  <section class="slide c1 r1">
    <div class="brand" style="left:90px;top:88px;">
      <span class="brand-mark"></span>
      <span class="brand-name">Vorstrup-Kjær<br>Consulting</span>
    </div>
  </section>

  <section class="slide c2 r1">
    <div class="photo" role="img" aria-label="Small seedling in a terracotta pot on a dark table" style="left:10px;top:13px;width:128px;height:190px;background:linear-gradient(160deg,#8d958d 0%,#5e6862 45%,#22282a 75%,#111 100%);"></div>
    <span class="tag" style="right:12px;top:12px;">Vorstrup-Kjær Consulting</span>
    <h2 class="title" style="left:181px;top:66px;">About Us</h2>
    <p class="body" style="left:181px;top:103px;width:165px;">We help founders and small teams turn bold ideas into next generation technology companies. From the first sketch to the first customer, our consultants work beside you on strategy, funding, product and hiring. We keep plans lean, decisions fast and growth steady, so you can spend your energy where it matters most: building the company you have always dreamed of.</p>
  </section>

  <section class="slide c3 r1">
    <div class="photo" role="img" aria-label="Team meeting around a whiteboard in a bright loft office" style="left:12px;top:11px;width:360px;height:109px;background:linear-gradient(100deg,#8c7a66 0%,#c9c3b9 40%,#e8e6e2 60%,#6b7580 85%,#3c4a5c 100%);"></div>
    <h2 class="title" style="left:14px;top:131px;font-size:21px;">About Us</h2>
    <p class="body" style="left:14px;top:160px;width:310px;">We help founders and small teams turn bold ideas into next generation technology companies. From the first sketch to the first customer, our consultants work beside you on strategy, funding, product and hiring. We keep plans lean, decisions fast and growth steady, so you can spend your energy where it matters most: building the company you have always dreamed of.</p>
    <span class="tag" style="right:13px;top:200px;">Vorstrup-Kjær Consulting</span>
  </section>

  <!-- Row 2 -->
  <section class="slide c1 r2">
    <span class="tag" style="left:8px;top:12px;">Vorstrup-Kjær Consulting</span>
    <h2 class="title" style="left:26px;top:61px;">Our Story</h2>
    <p class="body" style="left:26px;top:95px;width:146px;">We help founders and small teams turn bold ideas into next generation technology companies. From the first sketch to the first customer, our consultants work beside you on strategy, funding, product and hiring. We keep plans lean, decisions fast and growth steady, so you can spend your energy where it matters most: building the company you have always dreamed of.</p>
    <div class="photo" role="img" aria-label="Green grass blades over a ribbed golden surface" style="left:207px;top:0;width:177px;height:216px;background:linear-gradient(135deg,#d6b07a 0%,#c99a5a 45%,#a7a04a 70%,#c8a066 100%);"></div>
  </section>

  <section class="slide c2 r2">
    <h2 class="title" style="left:12px;top:13px;">Our Story</h2>
    <p class="body" style="left:12px;top:46px;width:290px;">Founded in Copenhagen, we began as a small group of engineers and advisers who wanted to make starting up simpler. Today we guide new technology ventures through every stage of early growth.</p>
    <div class="photo" role="img" aria-label="Young team working together on laptops at a shared desk" style="left:0;top:81px;width:270px;height:135px;background:linear-gradient(110deg,#3a3430 0%,#6d5d50 35%,#cfc9c2 55%,#4a4440 80%,#2a2624 100%);"></div>
    <span class="tag vertical" style="left:367px;top:80px;">Vorstrup-Kjær Consulting</span>
  </section>

  <section class="slide c3 r2">
    <div class="photo" role="img" aria-label="Portrait of the founder standing in an open office" style="left:0;top:0;width:150px;height:162px;background:linear-gradient(150deg,#6a6a66 0%,#8a8780 40%,#7b98b8 70%,#4e5d6e 100%);"></div>
    <h2 class="title" style="left:190px;top:75px;">VORSTRUP KJÆR</h2>
    <p class="body" style="left:190px;top:108px;width:150px;">Founder and lead adviser, helping new technology companies find their footing, raise capital and grow with confidence from day one.</p>
    <span class="tag vertical" style="left:367px;top:80px;">Vorstrup-Kjær Consulting</span>
  </section>

  <!-- Row 3 -->
  <section class="slide c1 r3">
    <h2 class="title" style="left:38px;top:27px;font-size:23px;">Our Team</h2>
    <div class="photo" role="img" aria-label="Team member portrait on a road" style="left:35px;top:69px;width:70px;height:78px;background:linear-gradient(180deg,#6b645c,#2f3a55);"></div>
    <div class="photo" role="img" aria-label="Team member portrait against a turquoise wall" style="left:114px;top:69px;width:70px;height:78px;background:linear-gradient(180deg,#5cc3d6,#9fb6cc);"></div>
    <div class="photo" role="img" aria-label="Team member portrait in a patterned shirt" style="left:192px;top:69px;width:70px;height:78px;background:linear-gradient(180deg,#4f5a38,#8a6a4a);"></div>
    <div class="photo" role="img" aria-label="Team member portrait among orange flowers" style="left:270px;top:69px;width:70px;height:78px;background:linear-gradient(180deg,#3f5a3a,#c98a5c);"></div>
    <p class="body" style="left:38px;top:156px;width:250px;">Our team brings together founders, engineers and investors who have built companies themselves. We share what worked, what failed and what we would do differently, so your start-up moves faster.</p>
    <span class="tag vertical" style="left:368px;top:78px;">Vorstrup-Kjær Consulting</span>
  </section>

  <section class="slide c2 r3">
    <div class="photo" role="img" aria-label="Analytics dashboard with cyan bar charts on a dark screen" style="left:12px;top:11px;width:331px;height:109px;background:linear-gradient(90deg,#1d2a22 0%,#06181d 10%,#0a3a44 35%,#07161b 55%,#0a3a44 80%,#06181d 100%);"></div>
    <div class="abs" style="left:343px;top:11px;width:22px;height:109px;background:linear-gradient(90deg,#fbeef2,#fff);"></div>
    <h2 class="title" style="left:18px;top:139px;">Monitoring</h2>
  </section>

  <section class="slide c3 r3">
    <svg class="chart" width="385" height="216" viewBox="0 0 385 216">
      <g stroke="var(--grid)" stroke-width="0.8">
        <line x1="81" y1="31" x2="271" y2="31"/><line x1="81" y1="51" x2="271" y2="51"/>
        <line x1="81" y1="71" x2="271" y2="71"/><line x1="81" y1="91" x2="271" y2="91"/>
        <line x1="81" y1="111" x2="271" y2="111"/><line x1="81" y1="132" x2="271" y2="132"/>
        <line x1="81" y1="152" x2="271" y2="152"/>
      </g>
      <g stroke="#999" stroke-width="0.8"><line x1="81" y1="31" x2="81" y2="172"/><line x1="81" y1="172" x2="271" y2="172"/></g>
      <g text-anchor="end">
        <text x="72" y="34">7</text><text x="72" y="54">6</text><text x="72" y="74">5</text><text x="72" y="94">4</text>
        <text x="72" y="114">3</text><text x="72" y="135">2</text><text x="72" y="155">1</text><text x="72" y="175">0</text>
      </g>
      <g text-anchor="middle">
        <text x="105" y="188">Text Here</text><text x="152" y="188">Text Here</text>
        <text x="199" y="188">Text Here</text><text x="246" y="188">text Here</text>
      </g>
      <polyline fill="none" stroke="var(--blue-light)" stroke-width="1.4" points="105,148 152,146 199,106 246,81"/>
      <polyline fill="none" stroke="var(--blue-dark)" stroke-width="1.4" points="105,86 152,122 199,102 246,81"/>
      <polyline fill="none" stroke="var(--blue-mid)" stroke-width="1.4" points="105,124 152,84 199,96 246,55"/>
      <g fill="var(--blue-dark)"><rect x="103" y="84" width="3" height="3"/><rect x="150" y="120" width="3" height="3"/><rect x="197" y="100" width="3" height="3"/></g>
      <g fill="var(--blue-mid)"><rect x="103" y="122" width="3" height="3"/><rect x="150" y="82" width="3" height="3"/><rect x="197" y="94" width="3" height="3"/><rect x="244" y="53" width="3" height="3"/></g>
      <g fill="var(--blue-light)"><rect x="103" y="146" width="3" height="3"/><rect x="150" y="144" width="3" height="3"/><rect x="244" y="79" width="3" height="3"/></g>
      <line x1="279" y1="93" x2="290" y2="93" stroke="var(--blue-dark)" stroke-width="1.4"/><text x="291" y="96">Lorem</text>
      <line x1="279" y1="107" x2="290" y2="107" stroke="var(--blue-mid)" stroke-width="1.4"/><text x="291" y="110">Ipsum</text>
      <line x1="279" y1="122" x2="290" y2="122" stroke="var(--blue-light)" stroke-width="1.4"/><text x="291" y="125">Here</text>
    </svg>
  </section>

  <!-- Row 4 -->
  <section class="slide c1 r4">
    <svg class="chart" width="384" height="216" viewBox="0 0 384 216">
      <g stroke="var(--grid)" stroke-width="0.8">
        <line x1="78" y1="31" x2="260" y2="31"/><line x1="78" y1="54" x2="260" y2="54"/>
        <line x1="78" y1="78" x2="260" y2="78"/><line x1="78" y1="101" x2="260" y2="101"/>
        <line x1="78" y1="124" x2="260" y2="124"/><line x1="78" y1="148" x2="260" y2="148"/>
      </g>
      <g stroke="#999" stroke-width="0.8"><line x1="78" y1="31" x2="78" y2="171"/><line x1="78" y1="171" x2="260" y2="171"/></g>
      <g text-anchor="end">
        <text x="72" y="34">6</text><text x="72" y="57">5</text><text x="72" y="81">4</text><text x="72" y="104">3</text>
        <text x="72" y="127">2</text><text x="72" y="151">1</text><text x="72" y="174">0</text>
      </g>
      <g fill="var(--blue-dark)">
        <rect x="89" y="71" width="9" height="100"/><rect x="134" y="113" width="9" height="58"/>
        <rect x="178" y="89" width="9" height="82"/><rect x="223" y="66" width="9" height="105"/>
      </g>
      <g fill="var(--blue-mid)">
        <rect x="99" y="115" width="9" height="56"/><rect x="144" y="68" width="9" height="103"/>
        <rect x="188" y="129" width="9" height="42"/><rect x="233" y="106" width="9" height="65"/>
      </g>
      <g fill="var(--blue-light)">
        <rect x="109" y="124" width="9" height="47"/><rect x="154" y="124" width="9" height="47"/>
        <rect x="198" y="101" width="9" height="70"/><rect x="243" y="54" width="9" height="117"/>
      </g>
      <g text-anchor="middle">
        <text x="104" y="186">Text 1</text><text x="149" y="186">Text 2</text>
        <text x="193" y="186">Text 3</text><text x="238" y="186">Text 4</text>
      </g>
      <rect x="270" y="89" width="5" height="5" fill="var(--blue-dark)"/><text x="278" y="95">Product 1</text>
      <rect x="270" y="104" width="5" height="5" fill="var(--blue-mid)"/><text x="278" y="110">Product 2</text>
      <rect x="270" y="119" width="5" height="5" fill="var(--blue-light)"/><text x="278" y="125">Product 3</text>
    </svg>
  </section>

  <section class="slide c2 r4">
    <svg class="chart" width="384" height="216" viewBox="0 0 384 216">
      <defs>
        <linearGradient id="cone-dark" x1="0" x2="1"><stop offset="0" stop-color="#2d4c86"/><stop offset="0.5" stop-color="#5b86c9"/><stop offset="1" stop-color="#274479"/></linearGradient>
        <linearGradient id="cone-mid" x1="0" x2="1"><stop offset="0" stop-color="#4a73b5"/><stop offset="0.5" stop-color="#8fb0e0"/><stop offset="1" stop-color="#41659f"/></linearGradient>
        <linearGradient id="cone-light" x1="0" x2="1"><stop offset="0" stop-color="#9fb1d4"/><stop offset="0.5" stop-color="#dbe4f3"/><stop offset="1" stop-color="#93a5c9"/></linearGradient>
      </defs>
      <g stroke="var(--grid)" stroke-width="0.7" fill="none">
        <polyline points="84,56 104,41 244,41"/><polyline points="84,133 104,118 244,118"/>
        <line x1="84" y1="72" x2="104" y2="57"/><line x1="104" y1="57" x2="244" y2="57"/>
        <line x1="84" y1="87" x2="104" y2="72"/><line x1="104" y1="72" x2="244" y2="72"/>
        <line x1="84" y1="102" x2="104" y2="87"/><line x1="104" y1="87" x2="244" y2="87"/>
        <line x1="84" y1="118" x2="104" y2="103"/><line x1="104" y1="103" x2="244" y2="103"/>
        <line x1="84" y1="56" x2="84" y2="133"/><line x1="104" y1="41" x2="104" y2="118"/>
        <polyline points="84,133 228,150 244,118"/>
      </g>
      <g text-anchor="end">
        <text x="74" y="57">5</text><text x="74" y="73">4</text><text x="74" y="89">3</text>
        <text x="74" y="104">2</text><text x="74" y="120">1</text><text x="74" y="136">0</text>
      </g>
      <g>
        <polygon points="135,91 129,115 141,115" fill="url(#cone-light)"/>
        <polygon points="163,83 157,115 169,115" fill="url(#cone-light)"/>
        <polygon points="191,79 185,115 197,115" fill="url(#cone-light)"/>
        <polygon points="222,50 216,119 228,119" fill="url(#cone-light)"/>
        <polygon points="119,91 113,122 125,122" fill="url(#cone-mid)"/>
        <polygon points="151,59 145,122 157,122" fill="url(#cone-mid)"/>
        <polygon points="193,83 187,122 199,122" fill="url(#cone-mid)"/>
        <polygon points="215,91 209,122 221,122" fill="url(#cone-mid)"/>
        <polygon points="112,66 105,127 119,127" fill="url(#cone-dark)"/>
        <polygon points="139,83 132,135 146,135" fill="url(#cone-dark)"/>
        <polygon points="183,99 176,127 190,127" fill="url(#cone-dark)"/>
        <polygon points="205,67 198,143 212,143" fill="url(#cone-dark)"/>
      </g>
      <g text-anchor="middle">
        <text x="102" y="152">Text</text><text x="102" y="163">Here</text>
        <text x="135" y="156">Text</text><text x="135" y="167">Here</text>
        <text x="166" y="159">Text</text><text x="166" y="170">Here</text>
        <text x="199" y="162">Text</text><text x="199" y="173">Here</text>
      </g>
      <text x="244" y="126">Dolor</text><text x="230" y="147">Lorem</text>
      <rect x="282" y="90" width="5" height="5" fill="var(--blue-dark)"/><text x="290" y="96">Lorem</text>
      <rect x="282" y="104" width="5" height="5" fill="var(--blue-mid)"/><text x="290" y="110">Ipsum</text>
      <rect x="282" y="119" width="5" height="5" fill="var(--blue-light)"/><text x="290" y="125">Dolor</text>
    </svg>
  </section>

  <section class="slide c3 r4">
    <h2 class="title" style="left:11px;top:14px;">Monitoring</h2>
    <p class="body" style="left:11px;top:47px;width:260px;">We track the numbers that matter, from traffic and sessions to revenue, so you always know where your company stands and what to improve next.</p>
    <div class="photo" role="img" aria-label="Laptop showing a growth analytics dashboard on a wooden desk" style="left:0;top:81px;width:270px;height:135px;background:linear-gradient(120deg,#2e3a4a 0%,#dfe6ec 40%,#9bc9c4 55%,#6e5a4a 80%,#3a2e28 100%);"></div>
    <span class="tag vertical" style="left:366px;top:78px;">Vorstrup-Kjær Consulting</span>
  </section>

  <!-- Row 5 -->
  <section class="slide c1 r5">
    <div class="photo" role="img" aria-label="Hands writing notes beside a laptop keyboard" style="left:10px;top:14px;width:127px;height:190px;background:linear-gradient(160deg,#7fa0a8 0%,#c6d1d2 35%,#e6e8e2 60%,#7d8a90 85%,#4b5559 100%);"></div>
    <span class="tag" style="right:14px;top:12px;">Vorstrup-Kjær Consulting</span>
    <h2 class="title" style="left:187px;top:75px;">Our Service</h2>
    <p class="body" style="left:187px;top:110px;width:150px;">From strategy workshops to investor meetings, we stand beside you at every step and turn ambitious plans into clear, practical actions.</p>
  </section>

  <section class="slide c2 r5">
    <div class="photo" role="img" aria-label="Red arrow pointing up on a grey concrete surface" style="left:12px;top:12px;width:360px;height:109px;background:linear-gradient(135deg,#e9e9e9 0%,#a9a9a9 30%,#c4302c 50%,#8f8f8f 65%,#bdbdbd 100%);"></div>
    <h2 class="title" style="left:18px;top:133px;">Our Service</h2>
    <p class="body" style="left:18px;top:170px;width:210px;">We offer hands-on support with business plans, funding rounds, product roadmaps and recruitment. Every engagement is shaped around your goals and the pace your company needs to grow.</p>
    <span class="tag" style="right:12px;top:201px;">Vorstrup-Kjær Consulting</span>
  </section>

  <section class="slide c3 r5">
    <div class="brand" style="left:90px;top:88px;">
      <span class="brand-mark"></span>
      <span class="brand-name">Vorstrup-Kjær<br>Consulting</span>
    </div>
  </section>

</div>
</body>
</html>
```